Morrow Pulse - Report on digital habits and attitudes

We are a research company and we have written a PowerPoint Report to present the results of a series of surveys conducted in the last three years. The research is about the "Morrow Pulse": people are facing the opportunities and challanges of their lives transformed by the digital technologies. We have investigated a number of topics through thousands of interviews and we've analyzed the data presented in the PowerPoint document.
We're not quite satisfied with the look and feel of the report: it looks too flat and boring, too "basic" to be presented as a professional work, yet being just that. We'd like you to upgrade the graphics and style of the report up to the level of a professional research product. The document still needs to be fully editable (either text and charts) but you can rearrange all the contents as you please, adding images, changing font and text size, colors and whatever you think is necessary to reach our goal.

Target Market(s)

Media covering digital issues
Marketing executives
Public institutions and policy makers

Industry/Entity Type

Market Research

Requirements
Must have
• The treats of a professional work
Fully editable within PowerPoint (either text and charts)
Nice to have
• Smart images
Original organization of the pages
Colors and graphics coherent with the torvenglade.it logo/website look and feel
Should not have
• PPT document over 30 MBytes
Images violating copyright

```html
<!DOCTYPE html>
<html lang="it">
<head>
<meta charset="utf-8">
<title>Morrow Pulse – Le paure</title>
<link href="https://fonts.googleapis.com/css2?family=Carlito:ital,wght@0,400;0,700;1,400;1,700&display=swap" rel="stylesheet">
<style>
  :root{
    --ink:#111;
    --muted:#44546a;
    --navy:#1f3864;
    --rule:#8497b0;
    --frame:#a6a6a6;
    --grid:#e4e4e4;
    --accent-top:#6f8f3a;
    --accent-bottom:#c9d6a3;
    --bar-black:#000;
    --bar-grey:#a6a6a6;
    --bar-blue:#0070c0;
    --footer-mark:#e07b1f;
  }
  *{margin:0;padding:0;box-sizing:border-box}
  html,body{width:760px;height:1200px;overflow:hidden;background:#fff}
  body{font-family:"Carlito",Calibri,sans-serif;color:var(--ink);position:relative}
  .page-title{position:absolute;left:48px;top:40px;height:28px;display:flex;align-items:center}
  .page-title .accent{width:7px;height:28px;background:linear-gradient(var(--accent-top),var(--accent-bottom));margin-right:12px}
  .page-title h1{font-weight:400;font-size:19px}
  .page-number{position:absolute;left:695px;top:48px;font-size:12px}
  .body-text{position:absolute;font-size:11px;line-height:36.6px;text-align:justify}
  .intro{left:52px;top:84px;width:658px}
  .intro p + p{margin-top:3px}
  .col-left{left:51px;top:600px;width:322px}
  .col-right{left:408px;top:600px;width:302px}
  .col-left p + p,.col-right p + p{margin-top:8px}
  .panel{position:absolute;border:1px solid var(--frame);border-radius:20px}
  .panel-title{position:absolute;top:-9px;left:50%;transform:translateX(-50%);background:#fff;padding:0 10px;font-size:12.5px;white-space:nowrap}
  .panel-note{position:absolute;left:13px;right:13px;border-top:1px solid var(--rule);text-align:center;font-style:italic;font-size:9px;padding-top:8px}
  .fears{left:46px;top:279px;width:667px;height:302px}
  .fears .panel-note{top:270px}
  .trend{left:48px;top:847px;width:667px;height:289px}
  .trend .panel-note{top:253px}
  svg{position:absolute;left:0;top:0}
  .footer{position:absolute;left:50px;top:1160px;display:flex;align-items:center;font-size:10px;gap:8px}
  .footer .mark{width:8px;height:8px;border-radius:50%;border:1.5px solid var(--footer-mark)}
</style>
</head>
<body>
  <div class="page-title"><span class="accent"></span><h1>Le paure</h1></div>
  <div class="page-number">2</div>

  <div class="body-text intro">
    <p>Il digitale può fare paura per le conseguenze che produce nelle capacità cognitive, nelle relazioni personali e sociali, fino a quelle internazionali. Molti non conoscono cosa c’è dietro e da dove vengono certe <b><i>magie della tecnologia</i></b>, alle quali ci siamo abituati e che non ci meravigliano più ma rimangono in gran parte incomprensibili.</p>
    <p>Inoltre, certi racconti sulle sorveglianza digitale e sui nuovi poteri che emergono dai dati ispirano un senso di sospetto condiviso da un’ampia maggioranza di individui.</p>
  </div>

  <section class="panel fears">
    <div class="panel-title">Le paure e i sospetti</div>
    <svg width="667" height="270" viewBox="0 0 667 270" font-family="Carlito, Calibri, sans-serif">
      <g font-size="8.6" fill="#222" text-anchor="end">
        <text x="509" y="33">Nell'ambiente connesso è più facile manipolare le persone</text>
        <text x="509" y="63">I ragazzi hanno notevoli problemi di socializzazione a causa del digitale</text>
        <text x="509" y="92">Alcuni servizi sanno tutto di noi: chi vediamo, cosa facciamo, cosa scriviamo e diciamo, anche quando non siamo online</text>
        <text x="509" y="122">I dispositivi che utilizzo mandano continuamente dati su di me a organizzazioni di cui ignoro l'esistenza</text>
        <text x="509" y="153">Le notizie online ci fanno perdere la capacità di distinguere il vero dal falso</text>
        <text x="509" y="183">Il digitale diminuisce la capacità di apprendimento a tutte le età</text>
        <text x="509" y="213">Le democrazie sono a rischio a causa della diffusione dell'online</text>
        <text x="509" y="243">Prossimamente ci sarà una guerra cibernetica fra Stati</text>
      </g>
      <g stroke="#bfbfbf" stroke-width="0.8">
        <line x1="520" y1="15" x2="520" y2="255"/>
        <line x1="520" y1="251" x2="628" y2="251"/>
        <line x1="514" y1="30" x2="520" y2="30"/><line x1="514" y1="60" x2="520" y2="60"/>
        <line x1="514" y1="89" x2="520" y2="89"/><line x1="514" y1="119" x2="520" y2="119"/>
        <line x1="514" y1="150" x2="520" y2="150"/><line x1="514" y1="180" x2="520" y2="180"/>
        <line x1="514" y1="210" x2="520" y2="210"/><line x1="514" y1="240" x2="520" y2="240"/>
      </g>
      <rect x="521" y="23.5" width="100" height="13" fill="var(--bar-black)"/>
      <rect x="521" y="53.5" width="94" height="13" fill="var(--bar-black)"/>
      <rect x="521" y="82.5" width="88" height="13" fill="var(--bar-grey)"/>
      <rect x="521" y="112.5" width="81" height="13" fill="var(--bar-grey)"/>
      <rect x="521" y="143.5" width="74" height="13" fill="var(--bar-blue)"/>
      <rect x="521" y="173.5" width="44" height="13" fill="var(--bar-grey)"/>
      <rect x="521" y="203.5" width="32" height="13" fill="var(--bar-blue)"/>
      <rect x="521" y="233.5" width="26" height="13" fill="var(--bar-black)"/>
      <g font-size="9.6" fill="#222">
        <text x="628" y="34">80%</text><text x="622" y="63">77%</text>
        <text x="616" y="92">75%</text><text x="610" y="121">71%</text>
        <text x="603" y="153">70%</text><text x="573" y="182">42%</text>
        <text x="560" y="212">35%</text><text x="554" y="242">33%</text>
      </g>
    </svg>
    <div class="panel-note">Incidenza sul totale campione dei Top2Box di accordo, in una scala a 5 passi (1.017 casi a novembre 2020)</div>
  </section>

  <div class="body-text col-left">
    <p>Il sospetto che il flusso di informazioni generato dalle tecnologie sia utilizzato con finalità di <b>controllo o manipolazione</b> è molto diffuso e riguarda otto individui sui dieci.</p>
    <p style="text-align:left">Il 77% si dichiara d’accordo con l‘affermazione secondo la quale il digitale crea <b>problemi di socialità</b> nei ragazzi e il dato aumenta tra le</p>
  </div>
  <div class="body-text col-right">
    <p style="text-align:left">persone oltre i 54 anni di età. Così come tra i meno giovani trova conferma l’idea, già piuttosto diffusa, che il digitale diminuisca le <b>capacità di apprendimento</b>.</p>
    <p>Le paure sulle conseguenze politiche e sociali del digitale sono più contenute ma riguardano pur sempre un terzo della popolazione.</p>
  </div>

  <section class="panel trend">
    <div class="panel-title">Il trend dell’indice di paura</div>
    <svg width="667" height="250" viewBox="0 0 667 250" font-family="Carlito, Calibri, sans-serif">
      <g stroke="var(--grid)" stroke-width="0.8">
        <line x1="19" y1="27" x2="651" y2="27"/><line x1="19" y1="55" x2="651" y2="55"/>
        <line x1="19" y1="82" x2="651" y2="82"/><line x1="19" y1="110" x2="651" y2="110"/>
        <line x1="19" y1="137" x2="651" y2="137"/><line x1="19" y1="165" x2="651" y2="165"/>
        <line x1="19" y1="193" x2="651" y2="193"/>
      </g>
      <g stroke="#d0d0d0" stroke-width="1">
        <line x1="19" y1="221" x2="651" y2="221"/>
        <line x1="19" y1="221" x2="19" y2="225"/><line x1="146" y1="221" x2="146" y2="225"/>
        <line x1="272" y1="221" x2="272" y2="225"/><line x1="399" y1="221" x2="399" y2="225"/>
        <line x1="525" y1="221" x2="525" y2="225"/><line x1="651" y1="221" x2="651" y2="225"/>
      </g>
      <path d="M81,152 C130,144 175,145 204,131 C245,110 290,55 332,55 C375,55 420,115 459,115 C500,118 540,104 587,98" fill="none" stroke="var(--navy)" stroke-width="1"/>
      <circle cx="81" cy="152" r="4" fill="var(--bar-black)"/>
      <circle cx="204" cy="131" r="4" fill="var(--bar-blue)"/>
      <circle cx="332" cy="55" r="4" fill="var(--bar-grey)"/>
      <circle cx="459" cy="115" r="4" fill="var(--bar-black)"/>
      <circle cx="587" cy="98" r="4" fill="var(--bar-blue)"/>
      <g font-size="11.5" fill="var(--muted)" text-anchor="middle">
        <text x="84" y="175">58%</text><text x="209" y="153">59%</text>
        <text x="336" y="78">62%</text><text x="462" y="137">60%</text>
        <text x="588" y="121">60%</text>
      </g>
      <g font-size="11" fill="var(--navy)" text-anchor="middle">
        <text x="82" y="240">Feb 19</text><text x="209" y="240">Ott 19</text>
        <text x="336" y="240">Feb 20</text><text x="462" y="240">Mag 20</text>
        <text x="588" y="240">Nov 20</text>
      </g>
    </svg>
    <div class="panel-note">L’indice di paura è ottenuto come media semplice dei Top2Box delle otto voci analizzate</div>
  </section>

  <footer class="footer">
    <span class="mark"></span>
    <span>|&nbsp;&nbsp; Morrow Pulse |&nbsp;&nbsp; dicembre 2020 |&nbsp;&nbsp; © Torvenglade 2020</span>
  </footer>
</body>
</html>
```